Business card design for a engineering company

I need a double sided business card design for my company "Verdmont Flow Solutions". The card will be used in Malaysia. Sleek and professional, with a little design flare to it.
Information to showcase:
1. Company logo
2. Name, title, phone, email address, website address
3. our products "Pumping technology, Valve & actuation, Air Moving Technology
Example:
Ravi Tanaka
Business manager
ravi.tanaka@verdmont-example.com
www.verdmont-example.com.my
- Pumping technology
- Valve & actuation
- Air moving technology
Target Market(s)
engineers, purchasing managers
Industry/Entity Type
Business
Contact Information for Business Card
Ravi Tanaka
Business manager
ravi.tanaka@verdmont-example.com
www.verdmont-example.com.my
- Pumping technology
- Valve & actuation
- Air moving technology
catch phrase : "Solving flow challenges, exceeding expectations"

```html
<!DOCTYPE html>
<html lang="en">
<head>
<meta charset="utf-8">
<title>Verdmont Flow Solutions – Business Card</title>
<link href="https://fonts.googleapis.com/css2?family=Roboto:wght@400;700&display=swap" rel="stylesheet">
<style>
  :root {
    --backdrop: #e9e7e4;
    --card: #ffffff;
    --ink: #1e2a36;
    --accent: #f29a1f;
    --muted: #5d6d7c;
  }
  * { box-sizing: border-box; margin: 0; padding: 0; }
  html, body { width: 1200px; height: 1200px; overflow: hidden; }
  body {
    background: var(--backdrop);
    font-family: "Roboto", Arial, sans-serif;
    position: relative;
  }
  .card {
    position: absolute;
    left: 100px; top: 314px;
    width: 1000px; height: 572px;
    background: var(--card);
    box-shadow: 0 6px 24px rgba(0,0,0,0.12);
  }
  .brand {
    position: absolute;
    left: 90px; top: 248px;
    display: flex; align-items: center; gap: 18px;
  }
  .brand-mark {
    width: 64px; height: 64px;
    background: var(--accent);
  }
  .brand-name {
    font-size: 30px; font-weight: 700;
    color: var(--ink);
    letter-spacing: 0.5px;
    line-height: 1.1;
  }
  .divider {
    position: absolute;
    left: 560px; top: 60px; bottom: 60px;
    width: 2px; background: var(--ink);
  }
  .person {
    position: absolute;
    left: 604px; top: 70px;
  }
  .person-name { font-size: 30px; font-weight: 700; color: var(--ink); }
  .person-title { font-size: 22px; color: var(--accent); margin-top: 2px; }
  .contacts {
    position: absolute;
    left: 604px; bottom: 84px;
    list-style: none;
  }
  .contacts li {
    display: flex; align-items: center; gap: 16px;
    font-size: 20px; color: var(--ink);
    height: 36px;
  }
  .icon {
    width: 24px; height: 24px; flex: none;
    background: var(--accent);
    display: flex; align-items: center; justify-content: center;
  }
  .icon svg { width: 16px; height: 16px; }
</style>
</head>
<body>
  <article class="card">
    <div class="brand">
      <span class="brand-mark"></span>
      <span class="brand-name">Verdmont Flow Solutions</span>
    </div>

    <div class="divider"></div>

    <header class="person">
      <h1 class="person-name">Ravi Tanaka</h1>
      <p class="person-title">Business manager</p>
    </header>

    <ul class="contacts">
      <li>
        <span class="icon"><svg viewBox="0 0 16 16"><path d="M4 2l2.5 3-1.5 1.5c.8 1.8 2.2 3.2 4 4L10.5 9 13.5 11.5 12 14C7 13.5 2.5 9 2 4z" fill="#fff"/></svg></span>
        (+6) 07 555 0142
      </li>
      <li>
        <span class="icon"><svg viewBox="0 0 16 16"><rect x="3" y="2" width="8" height="4" fill="none" stroke="#fff" stroke-width="1.4"/><rect x="2" y="6" width="12" height="7" fill="#fff"/><rect x="5" y="9" width="6" height="1.4" fill="#f29a1f"/></svg></span>
        (+6) 07 555 0178
      </li>
      <li>
        <span class="icon"><svg viewBox="0 0 16 16"><rect x="2" y="4" width="12" height="8" fill="none" stroke="#fff" stroke-width="1.4"/><path d="M2 4l6 5 6-5" fill="none" stroke="#fff" stroke-width="1.4"/></svg></span>
        ravi.tanaka@verdmont-example.com
      </li>
      <li>
        <span class="icon"><svg viewBox="0 0 16 16"><circle cx="8" cy="8" r="5.5" fill="none" stroke="#fff" stroke-width="1.4"/><ellipse cx="8" cy="8" rx="2.3" ry="5.5" fill="none" stroke="#fff" stroke-width="1.2"/><path d="M2.5 8h11" stroke="#fff" stroke-width="1.2"/></svg></span>
        www.verdmont-example.com.my
      </li>
    </ul>
  </article>
</body>
</html>
```